Vireo M.K. - Diagnostic Ultrasound Flyer

About US
Vireo M.K. is a concierge ultrasound company that provides onsite or offsite diagnostic ultrasounds. We have over 14 years experience in sonography, business management, and customer service. We offer both the physician and patient flexibility, convenience, and access to timely services.

We provide ultrasounds for the following specialties:
Obstetrics/Gynecology
Abdominal
Small Parts
Vascular

Company Features:
1. Onsite or Offsite Scans
2. Images Available Immediately for Referring Physician and Patient
3. Flexible Options for Ultrasound Interpretation/Billing
4. Access to Interpreting Radiologist
5. Final Report Process - 1-2 Business Days/ 1 hour for STAT.
6. PACS Storage with Secure Access.

We need a place to add in our contact information (address, email, website, phone)

We already have a logo and would like to use it ( they are attached). We would the colors to match the logo colors....maybe lighter version of yellow and blue.

```html
<!DOCTYPE html>
<html lang="en">
<head>
<meta charset="utf-8">
<title>Vireo M.K. – Diagnostic Ultrasound Flyer</title>
<link href="https://fonts.googleapis.com/css2?family=Fredoka:wght@500;600&family=Open+Sans:wght@400;600&display=swap" rel="stylesheet">
<style>
  :root{
    --blue:#5b7bc4;
    --blue-deep:#3b4fb2;
    --navy:#2a3a9e;
    --yellow:#f9b22a;
    --orange:#f39a1e;
    --white:#ffffff;
    --ink:#2b2b33;
    --rule:#c9cbd3;
    --page:#e9e9ea;
  }
  *{margin:0;padding:0;box-sizing:border-box}
  html,body{width:1200px;height:2187px;overflow:hidden;background:var(--page)}
  .flyer{
    position:absolute;left:30px;top:285px;width:790px;height:1120px;
    transform:scale(1.443);transform-origin:0 0;
    background:var(--white);overflow:hidden;
    font-family:"Open Sans",sans-serif;color:var(--ink);
  }
  .backdrop{position:absolute;inset:0}
  .brand{
    position:absolute;left:395px;top:62px;display:flex;align-items:center;gap:12px;
    font-family:"Fredoka",sans-serif;font-weight:600;font-size:46px;color:var(--navy);letter-spacing:1px;
  }
  .brand-dot{width:22px;height:22px;border-radius:50%;background:var(--orange)}
  .headline{
    position:absolute;left:72px;top:168px;
    font-family:"Fredoka",sans-serif;font-weight:600;font-size:52px;line-height:64px;color:var(--white);
  }
  .about{
    position:absolute;left:72px;top:308px;width:250px;
    font-size:16.5px;line-height:20.8px;color:var(--white);
  }
  .section-title{
    font-family:"Fredoka",sans-serif;font-weight:600;color:var(--orange);font-size:21px;line-height:29px;letter-spacing:.6px;
  }
  .specialties-title{position:absolute;left:72px;top:652px}
  .specialties{position:absolute;left:72px;top:736px;list-style:none}
  .specialties li{display:flex;align-items:center;gap:22px;height:56px;font-size:22px}
  .spec-icon{width:42px;height:42px;border-radius:50%;border:2px solid #fbe3b4;background:#fff6e2;display:flex;align-items:center;justify-content:center}
  .spec-icon span{width:18px;height:18px;border-radius:50%;border:2px solid var(--yellow)}
  .divider{position:absolute;left:393px;top:745px;width:1px;height:280px;background:var(--rule)}
  .features-title{position:absolute;left:418px;top:720px}
  .features{position:absolute;left:418px;top:758px;width:330px;list-style:none;font-size:16px;line-height:19px}
  .features li{display:flex;gap:8px;margin-bottom:18px}
  .features li b{color:var(--orange);font-weight:600}
  .cta{
    position:absolute;left:72px;top:983px;width:252px;height:42px;border-radius:0 22px 22px 0;
    background:var(--navy);color:var(--white);
    font-family:"Fredoka",sans-serif;font-weight:600;font-size:21px;letter-spacing:1px;
    display:flex;align-items:center;padding-left:24px;
  }
  .contact{
    position:absolute;left:72px;top:1066px;display:flex;align-items:center;
    font-family:"Fredoka",sans-serif;font-weight:600;font-size:20px;color:var(--ink);
  }
  .contact-item{display:flex;align-items:center;gap:8px;padding:0 14px}
  .contact-item:first-child{padding-left:0}
  .contact-item+.contact-item{border-left:1.5px solid rgba(255,255,255,.8)}
  .contact svg{width:20px;height:20px}
</style>
</head>
<body>
<main class="flyer">
  <svg class="backdrop" viewBox="0 0 790 1120" width="790" height="1120">
    <defs>
      <linearGradient id="footerGrad" x1="0" x2="1" y1="0" y2="0">
        <stop offset="0" stop-color="#f7a21f"/><stop offset="1" stop-color="#fbbd2e"/>
      </linearGradient>
      <linearGradient id="scanGrad" x1="0" x2="1" y1="0" y2="1">
        <stop offset="0" stop-color="#eef0f4"/><stop offset=".55" stop-color="#d9c3b3"/><stop offset="1" stop-color="#6f86b8"/>
      </linearGradient>
      <linearGradient id="clinicGrad" x1="0" x2="1" y1="0" y2="1">
        <stop offset="0" stop-color="#4c6f78"/><stop offset=".5" stop-color="#c9d2d6"/><stop offset="1" stop-color="#d6b89e"/>
      </linearGradient>
    </defs>
    <path d="M470,0 C560,40 640,90 790,50 L790,0 Z" fill="#f1f2f6"/>
    <path d="M790,120 C690,140 620,180 590,210 L690,620 C735,650 770,690 790,700 Z" fill="var(--blue)"/>
    <path d="M790,330 C760,420 740,520 700,600 L790,690 Z" fill="var(--blue-deep)"/>
    <path d="M0,140 C110,72 300,72 430,165 L560,300 L540,520 C420,610 200,640 0,520 Z" fill="var(--blue)"/>
    <path d="M0,520 C200,640 420,610 540,520 C420,630 190,650 0,600 Z" fill="var(--yellow)"/>
    <path d="M0,1045 C210,1000 520,1060 790,990 L790,1120 L0,1120 Z" fill="url(#footerGrad)"/>
    <circle cx="562" cy="362" r="222" fill="var(--white)"/>
    <circle cx="562" cy="362" r="216" fill="var(--yellow)"/>
    <circle cx="562" cy="362" r="206" fill="url(#scanGrad)" role="img" aria-label="Photo: sonographer scanning a pregnant patient's abdomen"/>
    <circle cx="492" cy="562" r="140" fill="var(--white)"/>
    <circle cx="492" cy="562" r="132" fill="url(#clinicGrad)" role="img" aria-label="Photo: clinician reviewing an ultrasound monitor beside a patient"/>
  </svg>

  <div class="brand"><span class="brand-dot"></span>Vireo M.K.</div>

  <h1 class="headline">Diagnostic<br>Ultrasound</h1>
  <p class="about">Vireo M.K. is a concierge ultrasound company that provides onsite or offsite diagnostic ultrasounds. We have over 14 years experience in sonography, business management, and customer service. We offer both the physician and patient flexibility, convenience, and access to timely services.</p>

  <h2 class="section-title specialties-title">We provide ultrasounds<br>for the following specialties:</h2>
  <ul class="specialties">
    <li><span class="spec-icon"><span></span></span>Obstetrics/Gynecology</li>
    <li><span class="spec-icon"><span></span></span>Abdominal</li>
    <li><span class="spec-icon"><span></span></span>Small Parts</li>
    <li><span class="spec-icon"><span></span></span>Vascular</li>
  </ul>

  <div class="divider"></div>

  <h2 class="section-title features-title">Company Features:</h2>
  <ol class="features">
    <li><b>1.</b><span>Onsite or Offsite Scans</span></li>
    <li><b>2.</b><span>Images Available Immediately for Referring Physician and Patient</span></li>
    <li><b>3.</b><span>Flexible Options for Ultrasound Interpretation/Billing</span></li>
    <li><b>4.</b><span>Access to Interpreting Radiologist</span></li>
    <li><b>5.</b><span>Final Report Process - 1-2 Business Days/ 1 hour for STAT.</span></li>
    <li><b>6.</b><span>PACS Storage with Secure Access.</span></li>
  </ol>

  <div class="cta">Contact us now!</div>

  <div class="contact">
    <div class="contact-item">
      <svg viewBox="0 0 24 24" fill="none" stroke="#2b2b33" stroke-width="1.8"><path d="M5 3h4l2 5-2.5 1.5a11 11 0 0 0 6 6L16 13l5 2v4a2 2 0 0 1-2 2A17 17 0 0 1 3 5a2 2 0 0 1 2-2z"/></svg>
      5550142873
    </div>
    <div class="contact-item">
      <svg viewBox="0 0 24 24" fill="none" stroke="#2b2b33" stroke-width="1.8"><circle cx="12" cy="12" r="9"/><path d="M3 12h18M12 3c3 3 3 15 0 18M12 3c-3 3-3 15 0 18"/></svg>
      www.vireomk.com
    </div>
    <div class="contact-item">
      <svg viewBox="0 0 24 24" fill="none" stroke="#2b2b33" stroke-width="1.8"><rect x="3" y="5" width="18" height="14" rx="1"/><path d="M3 6l9 7 9-7"/></svg>
      info@vireomk.com
    </div>
  </div>
</main>
</body>
</html>
```